Business Card Design Project

Im an electrician and my company name is Kestrel Electrical
My main work is installing Lighting and Power Points, Home Theater Systems, TVS, Phones and Data
Im looking a business card, something nice, clean, modern and not to cluttered
Im open to sugestions
I dont mind if the "Services" is on the back on the business card
colours black, grey, white or the blue colour of my logo are prefered but not compulsory
any questions just message me
and please make it so if i need to edit the writing can do it easy. maybe by making it a seperate layer ?
My Details are.
Name - Peter Halloran
Job Title - Licenced Electrician
Mobile - 027 583 2174
Email - peter@kestrelelectrical.co.nz
Web - www.kestrelelectrical.co.nz
Services
Residential / Commercial
Lighting & Power
Heating & Ventilation
Automation
Phone & Data
Home Cinema
Sound Systems
TV, Antenna & Satellite
Digital Upgrades

```html
<!DOCTYPE html>
<html lang="en">
<head>
<meta charset="utf-8">
<title>Kestrel Electrical – Business Card</title>
<link rel="stylesheet" href="https://fonts.googleapis.com/css2?family=Open+Sans:ital,wght@0,400;0,600;0,700;1,400;1,700&display=swap">
<style>
  :root {
    --teal: #00b2c9;
    --ink: #3a3d42;
    --card-white: #fbfbfb;
    --paper: #f1f1f1;
    --white: #ffffff;
  }
  * { box-sizing: border-box; margin: 0; padding: 0; }
  html, body {
    width: 1200px;
    height: 1000px;
    overflow: hidden;
    background: var(--paper);
    font-family: "Open Sans", Arial, sans-serif;
  }
  .canvas {
    position: relative;
    width: 1200px;
    height: 1000px;
  }
  .card {
    position: absolute;
    top: 358px;
    width: 456px;
    height: 284px;
    box-shadow: 0 2px 6px rgba(0,0,0,0.18);
  }

  /* Front */
  .card-front {
    left: 100px;
    background: var(--card-white);
  }
  .brand {
    position: absolute;
    left: 104px;
    top: 108px;
    display: flex;
    align-items: center;
    gap: 12px;
  }
  .brand-mark {
    width: 30px;
    height: 30px;
    background: var(--teal);
  }
  .brand-name {
    color: var(--teal);
    font-weight: 700;
    font-size: 22px;
    letter-spacing: 1px;
    line-height: 1.05;
    text-transform: uppercase;
  }
  .contact {
    position: absolute;
    right: 44px;
    top: 228px;
    text-align: right;
    font-size: 11.5px;
    color: var(--ink);
    line-height: 16px;
  }
  .contact .sep { color: var(--teal); padding: 0 2px; }
  .contact .label { color: var(--teal); font-style: italic; }
  .contact .bolt { display: inline-block; vertical-align: -1px; margin: 0 2px; }

  /* Back */
  .card-back {
    left: 644px;
    background: var(--teal);
    color: var(--white);
  }
  .back-name {
    position: absolute;
    left: 78px;
    top: 116px;
    font-weight: 700;
    font-size: 28px;
    line-height: 1.1;
    color: var(--white);
    text-transform: uppercase;
  }
  .services-label {
    position: absolute;
    left: 176px;
    top: 64px;
    font-weight: 700;
    font-style: italic;
    font-size: 12px;
  }
  .rule {
    position: absolute;
    height: 1px;
    background: var(--white);
    opacity: 0.9;
  }
  .rule-top { left: 256px; top: 72px; width: 92px; }
  .rule-bottom { left: 258px; top: 220px; width: 88px; }
  .services {
    position: absolute;
    left: 220px;
    top: 78px;
    width: 164px;
    list-style: none;
    text-align: center;
    font-size: 12px;
    line-height: 15px;
  }
</style>
</head>
<body>
<main class="canvas">

  <section class="card card-front" aria-label="Business card front">
    <div class="brand">
      <span class="brand-mark"></span>
      <span class="brand-name">Kestrel<br>Electrical</span>
    </div>
    <div class="contact">
      <p>Peter Halloran <span class="sep">|</span> Licenced Electrician <span class="sep">|</span> 027 583 2174</p>
      <p>
        <span class="label">email</span> peter@kestrelelectrical.co.nz
        <svg class="bolt" width="7" height="11" viewBox="0 0 7 11" aria-hidden="true"><path d="M4 0 L0 6 H3 L2 11 L7 4 H4 Z" fill="var(--teal)"/></svg>
        <span class="label">web</span> www.kestrelelectrical.co.nz
      </p>
    </div>
  </section>

  <section class="card card-back" aria-label="Business card back">
    <div class="back-name">Kestrel<br>Electrical</div>
    <p class="services-label">Services</p>
    <span class="rule rule-top"></span>
    <ul class="services">
      <li>Residential / Commercial</li>
      <li>Lighting &amp; Power</li>
      <li>Heating &amp; Ventilation</li>
      <li>Automation</li>
      <li>Phone &amp; Data</li>
      <li>Home Cinema</li>
      <li>Sound Systems</li>
      <li>TV, Antenna &amp; Satellite</li>
      <li>Digital Upgrades</li>
    </ul>
    <span class="rule rule-bottom"></span>
  </section>

</main>
</body>
</html>
```